Develop name logo for new consulting firm

The Larchmont Group is the name of the firm. I selected that name as I am related to Edmund Hale Porter. The purpose of the firm is to conduct healthcare and management consulting. We are based in the Washington, DC area.

I desire a sophisticated look...simple, but sophisticated.

Industry/Entity Type

Healthcare

```html
<!DOCTYPE html>
<html lang="en">
<head>
<meta charset="utf-8">
<title>The Larchmont Group — Letterhead</title>
<link rel="stylesheet" href="https://fonts.googleapis.com/css2?family=Didact+Gothic&display=swap">
<style>
  :root {
    --backdrop: #e6e7e6;
    --paper: #ffffff;
    --brand-green: #5b7a2c;
    --web-green: #6a9a2a;
    --ink-grey: #8a8c8c;
    --ink-dark: #6f7171;
    --rule-grey: #b9bbbb;
  }
  * { margin: 0; padding: 0; box-sizing: border-box; }
  html, body {
    width: 1200px;
    height: 955px;
    overflow: hidden;
    background: var(--backdrop);
  }
  .letterhead {
    position: absolute;
    left: 268px;
    top: 46px;
    width: 664px;
    height: 862px;
    background: var(--paper);
    box-shadow: 0 1px 3px rgba(0,0,0,0.08);
  }
  .brand-name {
    position: absolute;
    left: 44px;
    top: 132px;
    display: flex;
    align-items: center;
    gap: 10px;
    color: var(--brand-green);
    font-family: "Didact Gothic", sans-serif;
    font-weight: 400;
    font-size: 20px;
    line-height: 24px;
    letter-spacing: 0.3px;
    white-space: nowrap;
  }
  .brand-square {
    width: 14px;
    height: 14px;
    background: var(--brand-green);
  }
  .edge-tab {
    position: absolute;
    right: 0;
    top: 318px;
    width: 64px;
    height: 14px;
    background: var(--brand-green);
  }
  .contact-block {
    position: absolute;
    left: 388px;
    bottom: 66px;
    display: flex;
    gap: 12px;
    font-family: "Didact Gothic", sans-serif;
    font-size: 9.5px;
    line-height: 12px;
    color: var(--ink-grey);
  }
  .contact-rule {
    width: 1px;
    background: var(--rule-grey);
  }
  .contact-group + .contact-group { margin-top: 9px; }
  .contact-label { color: var(--ink-dark); font-weight: 700; }
  .web-accent { color: var(--web-green); font-weight: 700; }
</style>
</head>
<body>
  <main class="letterhead">
    <div class="brand-name"><span class="brand-square"></span>The Larchmont Group</div>
    <div class="edge-tab"></div>
    <footer class="contact-block">
      <div class="contact-rule"></div>
      <div class="contact-text">
        <div class="contact-group">
          418 Alder Crest Ln.<br>
          Suite 210<br>
          Bethesda<br>
          MD 20814
        </div>
        <div class="contact-group">
          <span class="contact-label">Phone:</span> (301) 555-0187<br>
          <span class="contact-label">Email:</span> info@larchmontgroup.com
        </div>
        <div class="contact-group">
          www.<span class="web-accent">larchmontgroup</span>.com
        </div>
      </div>
    </footer>
  </main>
</body>
</html>
```